Wallpaper für Partner für ganzheitliche IT-Infrastruktur-Lösungen
Zielgruppe
Wir sind Partner für ganzheitliche IT-Infrastruktur-Lösungen. Wir übernehmen technische Verantwortung für stabile, sichere und wirtschaftliche IT‑Systeme – von der Konzeption über den Betrieb bis zur langfristigen Betreuung. Unsere Zielgruppe sind kleine und mittelständische Unternehmen und Organisationen, die ihre IT als strategischen Erfolgsfaktor verstehen und Wert auf durchdachte Gesamtlösungen statt auf Stückwerk legen.
Aufgabenstellung
Es soll ein Wallpaper erstellt werden, das die bestehende CI ergänzt.
Das Design soll Verantwortung, Kompetenz und Verlässlichkeit ausstrahlen. Gesucht ist eine professionelle, aber zugängliche Optik, die ganzheitliches Denken und technische Stabilität vermittelt. Der Stil sollte modern, aber zeitlos sein – keine kurzlebigen Trends oder oberflächliche Tech-Klischees. Wichtig sind klare Strukturen und hochwertige Ästhetik, die Vertrauen schafft. Das NK-VR-Logo oder -Icon soll harmonisch in das Design integriert werden. Technische Anforderungen: Der Wallpaper muss sowohl im 16:9- als auch im 9:16-Format funktionieren und vollständig als Vektorgrafik ohne Rastereffekte geliefert werden.

```html
<!DOCTYPE html>
<html lang="de">
<head>
<meta charset="utf-8">
<title>NK-VR – Ganzheitliche IT-Infrastruktur-Lösungen</title>
<link rel="stylesheet" href="https://fonts.googleapis.com/css2?family=Montserrat:wght@700&display=swap">
<style>
  :root {
    --bg-teal: #113f47;
    --bg-teal-light: #184b53;
    --bg-teal-deep: #0e363e;
    --headline: #ececec;
    --brand-red: #d9472f;
  }
  html, body {
    margin: 0;
    padding: 0;
    width: 1200px;
    height: 1200px;
    overflow: hidden;
    background: var(--bg-teal);
  }
  .wallpaper {
    position: relative;
    width: 1200px;
    height: 1200px;
    overflow: hidden;
    background: var(--bg-teal);
    font-family: "Montserrat", Arial, sans-serif;
  }
  .circuit-backdrop {
    position: absolute;
    inset: 0;
    background:
      radial-gradient(ellipse 70% 60% at 50% 62%, var(--bg-teal-light) 0%, var(--bg-teal) 55%, var(--bg-teal-deep) 100%);
  }
  .headline {
    position: absolute;
    top: 196px;
    left: 0;
    width: 100%;
    margin: 0;
    text-align: center;
    color: var(--headline);
    font-weight: 700;
    font-size: 89px;
    line-height: 110px;
    letter-spacing: 0.025em;
    text-transform: uppercase;
    white-space: nowrap;
  }
  .headline span {
    display: block;
  }
  .brand {
    position: absolute;
    top: 700px;
    left: 0;
    width: 100%;
    height: 170px;
    display: flex;
    justify-content: center;
    align-items: center;
    gap: 34px;
  }
  .brand-mark {
    width: 44px;
    height: 44px;
    background: var(--brand-red);
  }
  .brand-name {
    color: var(--brand-red);
    font-weight: 700;
    font-size: 160px;
    line-height: 1;
    letter-spacing: 0.02em;
  }
</style>
</head>
<body>
  <main class="wallpaper">
    <div class="circuit-backdrop" role="img" aria-label="Dezentes Muster aus Leiterbahnen in dunklem Petrol über die ganze Fläche"></div>
    <h1 class="headline">
      <span>Ganzheitliche</span>
      <span>IT-Infrastruktur-</span>
      <span>Lösungen</span>
    </h1>
    <div class="brand">
      <div class="brand-mark"></div>
      <div class="brand-name">NK-VR</div>
    </div>
  </main>
</body>
</html>
```